Real Estate For Sale Sign

I need to design a for sale sign. It needs to include The following information
Logo: Attached
Name: Corinne Vasquel,
Company Name: Gilded Harbor Real Estate,
Phone Number: 503-841-2096
BRE Licence Number 04817359 (Can Be small)
Sign size 24x30

I am not sure about including my website but I would like to see options with it. www.gildedharbor-example.com
Updates

Target Market(s)

Potential Buyers or Sellers of Real Estate. Must be easy to read.

Industry/Entity Type

Real Estate

Requirements
Must have
• I want it to feel luxurious and sharp.

```html
<!DOCTYPE html>
<html lang="en">
<head>
<meta charset="utf-8">
<title>Gilded Harbor Real Estate – For Sale Sign</title>
<link href="https://fonts.googleapis.com/css2?family=Bebas+Neue&family=Cinzel:wght@500;600&display=swap" rel="stylesheet">
<style>
  :root{
    --backdrop:#e9ebee;
    --paper:#ffffff;
    --navy:#0f1a3a;
    --ink:#1c2a52;
    --cyan:#1ba6dc;
    --blue:#1f5fa8;
    --grey-band:#e3e5e9;
    --grey-text:#7b8190;
  }
  *{box-sizing:border-box;margin:0;padding:0}
  html,body{width:1200px;height:900px;overflow:hidden;background:var(--backdrop)}
  .sign{
    position:absolute;left:162px;top:51px;width:876px;height:798px;
    background:var(--paper);box-shadow:0 6px 24px rgba(0,0,0,.18);
    display:flex;flex-direction:column;
  }
  .brand-head{
    height:210px;display:flex;align-items:center;padding-left:56px;gap:30px;
  }
  .brand-mark{width:112px;height:112px;border-radius:50%;background:var(--cyan);flex:none}
  .brand-name{font-family:"Cinzel",serif;font-weight:600;color:var(--ink);line-height:1}
  .brand-name .line1{display:block;font-size:64px;letter-spacing:2px}
  .brand-name .line2{display:block;font-size:30px;letter-spacing:10px;margin-top:10px;padding-left:150px}
  .message{
    height:434px;background:var(--navy);padding:30px 0 0 60px;color:#fff;
  }
  .headline{font-family:"Bebas Neue",sans-serif;font-size:150px;line-height:.9;letter-spacing:1px}
  .call{display:flex;align-items:baseline;gap:18px;margin-top:6px}
  .call .label{font-family:"Bebas Neue",sans-serif;font-size:70px;color:var(--cyan);letter-spacing:2px}
  .call .agent{font-family:"Cinzel",serif;font-weight:600;font-size:62px;color:#fff}
  .phone{font-family:"Bebas Neue",sans-serif;font-size:158px;line-height:.95;color:var(--cyan);letter-spacing:3px}
  .company{
    height:112px;display:flex;align-items:center;justify-content:center;
    font-family:"Cinzel",serif;font-weight:600;font-size:50px;color:var(--ink);
  }
  .footer-band{position:relative;height:42px;background:var(--grey-band)}
  .licence{
    position:absolute;left:40px;top:0;height:42px;line-height:42px;
    font-family:"Cinzel",serif;font-size:16px;color:var(--grey-text);letter-spacing:1px;
  }
  .web{
    position:absolute;right:0;top:0;height:42px;width:520px;background:var(--blue);
    clip-path:polygon(40px 0,100% 0,100% 100%,0 100%);
    display:flex;align-items:center;justify-content:flex-end;padding-right:26px;
    font-family:"Cinzel",serif;font-weight:500;font-size:24px;color:#fff;
  }
</style>
</head>
<body>
  <main class="sign">
    <header class="brand-head">
      <span class="brand-mark"></span>
      <div class="brand-name"><span class="line1">GILDED HARBOR</span><span class="line2">REAL ESTATE</span></div>
    </header>
    <section class="message">
      <h1 class="headline">HOUSE FOR SALE</h1>
      <p class="call"><span class="label">CALL</span><span class="agent">Corinne Vasquel</span></p>
      <p class="phone">503-841-2096</p>
    </section>
    <p class="company">Gilded Harbor Real Estate</p>
    <footer class="footer-band">
      <span class="licence">BRE LICENSE 04817359</span>
      <span class="web">www.gildedharbor-example.com</span>
    </footer>
  </main>
</body>
</html>
```